Financial Services Postcard Design

Lionel Budwig, CPA
Financial Services
Accounting/Tax/Consulting
Services include but not limited to
Financial Statements
Tax Returns
CFO/Controller services
Budgeting and Forecasting
Cash Management
Payroll / AP/ AR
Insurance Analysis
Cost Analysis
Special projects

I need a postcard design for my new financial service company to assist businesses in the Orange County area of southern California. I'm looking for a warm but bright look to represent CPA with many years of Management experience with manufacturing companies that can relate to business issues and provide solutions for small business.

```html
<!DOCTYPE html>
<html lang="en">
<head>
<meta charset="utf-8">
<title>Lionel Budwig, CPA – Financial Services Postcard</title>
<link rel="stylesheet" href="https://fonts.googleapis.com/css2?family=Oswald:wght@400;500;600&family=Cinzel:wght@600;700&family=Lato:wght@400;700&display=swap">
<style>
  :root {
    --page-bg: #e4e4e4;
    --card-white: #ffffff;
    --paper-grey: #eceef1;
    --royal-blue: #1f4fc4;
    --deep-blue: #12329a;
    --light-blue: #3e72e0;
    --brand-red: #e2202c;
    --ink: #222326;
    --ink-soft: #3a3d44;
    --line-grey: #4a4a4a;
  }
  * { box-sizing: border-box; margin: 0; padding: 0; }
  html, body { width: 772px; height: 1200px; overflow: hidden; }
  body { background: var(--page-bg); position: relative; font-family: 'Lato', sans-serif; }

  .postcard {
    position: absolute; left: 40px; width: 693px; height: 497px;
    background: var(--card-white); overflow: hidden;
    box-shadow: 0 2px 8px rgba(0,0,0,0.18);
  }
  .postcard--front { top: 64px; }
  .postcard--back { top: 629px; }
  .postcard svg.art { position: absolute; left: 0; top: 0; }

  /* front */
  .contact-badge {
    position: absolute; left: 384px; top: 160px; width: 160px; height: 160px;
    display: flex; flex-direction: column; align-items: center; justify-content: center;
    font-family: 'Oswald', sans-serif; text-transform: uppercase; line-height: 1;
    white-space: nowrap; text-align: center;
  }
  .contact-badge__top { color: var(--ink); font-size: 25px; font-weight: 500; letter-spacing: 0.3px; }
  .contact-badge__main { color: var(--brand-red); font-size: 42px; font-weight: 600; margin-top: 4px; }

  .front-name {
    position: absolute; right: 40px; top: 342px;
    font-family: 'Oswald', sans-serif; font-weight: 500; font-size: 44px;
    color: #fff; line-height: 1; text-transform: uppercase; letter-spacing: 0.3px;
    text-shadow: 0 2px 3px rgba(0,0,0,0.35); white-space: nowrap;
  }
  .front-tagline {
    position: absolute; right: 42px; top: 398px;
    font-family: 'Cinzel', serif; font-weight: 600; font-size: 28px; color: #fff;
    line-height: 1; letter-spacing: 0.5px; white-space: nowrap;
  }
  .social-row {
    position: absolute; right: 36px; top: 466px;
    display: flex; align-items: center; gap: 8px;
    font-family: 'Lato', sans-serif; color: #fff; font-size: 10px; font-weight: 700;
  }
  .social-row__label { font-family: 'Cinzel', serif; font-size: 10px; }

  /* back */
  .service-list {
    position: absolute; top: 22px; list-style: none;
    font-family: 'Lato', sans-serif; font-size: 12px; color: var(--ink-soft);
  }
  .service-list--left { left: 50px; }
  .service-list--right { left: 263px; }
  .service-list li { height: 23.2px; display: flex; align-items: center; gap: 9px; white-space: nowrap; }
  .service-list svg { flex: none; }

  .back-headline {
    position: absolute; left: 0; width: 447px; top: 272px; text-align: center;
    font-family: 'Oswald', sans-serif; font-weight: 600; font-size: 31px;
    color: var(--brand-red); line-height: 1; letter-spacing: 0.3px;
    text-shadow: 0 0 2px #fff, 0 0 1px #fff; white-space: nowrap;
  }
  .back-subline {
    position: absolute; left: 0; width: 447px; top: 308px; text-align: center;
    font-family: 'Cinzel', serif; font-weight: 700; font-size: 14px; color: #fff;
    line-height: 1; text-transform: uppercase; white-space: nowrap;
  }
  .back-contact { position: absolute; left: 120px; top: 343px; color: #fff; white-space: nowrap; }
  .back-contact__name {
    font-family: 'Oswald', sans-serif; font-weight: 500; font-size: 18px;
    color: var(--brand-red); line-height: 1.2;
  }
  .back-contact__line { font-family: 'Lato', sans-serif; font-size: 13.5px; line-height: 1; margin-top: 10px; }
  .back-contact__line + .back-contact__line { margin-top: 13px; }

  .stamp-box {
    position: absolute; left: 603px; top: 34px; width: 49px; height: 63px;
    border: 1.5px solid var(--line-grey);
  }
  .address-line {
    position: absolute; left: 475px; width: 177px; height: 0;
    border-top: 1.5px solid var(--line-grey);
  }
</style>
</head>
<body>

<section class="postcard postcard--front" aria-label="Postcard front">
  <svg class="art" width="693" height="497" viewBox="0 0 693 497">
    <defs>
      <linearGradient id="frontPaper" x1="0" y1="0" x2="0" y2="1">
        <stop offset="0" stop-color="#f4f5f7"/>
        <stop offset="1" stop-color="#dfe2e7"/>
      </linearGradient>
      <linearGradient id="deskPhoto" x1="0" y1="0" x2="1" y2="1">
        <stop offset="0" stop-color="#dfe6ef"/>
        <stop offset="0.5" stop-color="#c9d2dc"/>
        <stop offset="1" stop-color="#8d97a4"/>
      </linearGradient>
      <radialGradient id="frontBlue" cx="0.65" cy="0.35" r="0.8">
        <stop offset="0" stop-color="#3b6fe0"/>
        <stop offset="0.6" stop-color="#1f4fc4"/>
        <stop offset="1" stop-color="#12329a"/>
      </radialGradient>
      <linearGradient id="teamPhoto" x1="0" y1="0" x2="0" y2="1">
        <stop offset="0" stop-color="#b58a72"/>
        <stop offset="0.35" stop-color="#d9b49c"/>
        <stop offset="0.55" stop-color="#2d3140"/>
        <stop offset="1" stop-color="#14161d"/>
      </linearGradient>
    </defs>

    <rect width="693" height="497" fill="url(#frontPaper)"/>

    <g fill="#ffffff" opacity="0.9">
      <rect x="18" y="140" width="8" height="90"/>
      <rect x="32" y="120" width="8" height="110"/>
      <rect x="46" y="150" width="8" height="80"/>
      <rect x="60" y="105" width="8" height="125"/>
      <rect x="74" y="130" width="8" height="100"/>
      <rect x="610" y="190" width="8" height="50"/>
      <rect x="624" y="175" width="8" height="65"/>
      <rect x="638" y="160" width="8" height="80"/>
      <rect x="652" y="180" width="8" height="60"/>
      <rect x="666" y="150" width="8" height="90"/>
    </g>

    <polygon role="img" aria-label="Photo: hands working with a calculator, pen and financial papers on a desk"
             points="38,0 693,0 693,112 464,250" fill="url(#deskPhoto)"/>

    <rect x="0" y="240" width="693" height="215" fill="url(#frontBlue)"/>
    <polygon points="300,240 464,300 620,240" fill="#3b6fe0" opacity="0.5"/>

    <line x1="20" y1="-6" x2="440" y2="246" stroke="#ffffff" stroke-width="6"/>
    <line x1="8" y1="-2" x2="430" y2="252" stroke="var(--brand-red)" stroke-width="9"/>
    <line x1="26" y1="0" x2="446" y2="240" stroke="var(--royal-blue)" stroke-width="6"/>
    <line x1="490" y1="245" x2="700" y2="114" stroke="#ffffff" stroke-width="6"/>
    <line x1="495" y1="252" x2="705" y2="120" stroke="var(--brand-red)" stroke-width="9"/>
    <line x1="484" y1="238" x2="700" y2="104" stroke="var(--royal-blue)" stroke-width="6"/>

    <rect x="0" y="451" width="693" height="46" fill="var(--brand-red)"/>

    <rect role="img" aria-label="Photo: smiling businesswoman and businessman in suits"
          x="0" y="215" width="300" height="282" fill="url(#teamPhoto)"/>

    <circle cx="464" cy="240" r="86" fill="var(--royal-blue)"/>
    <circle cx="464" cy="240" r="79" fill="#ffffff"/>
  </svg>

  <div class="contact-badge">
    <span class="contact-badge__top">Contact us</span>
    <span class="contact-badge__main">Today</span>
  </div>

  <h1 class="front-name">Lionel Budwig, CPA</h1>
  <p class="front-tagline">Financial Services</p>

  <div class="social-row">
    <span class="social-row__label">LIKE US</span>
    <span>Friendsly</span>
    <span>Chirpa</span>
    <span>Circlo</span>
  </div>
</section>

<section class="postcard postcard--back" aria-label="Postcard back">
  <svg class="art" width="447" height="440" viewBox="0 0 447 440">
    <defs>
      <linearGradient id="backPaper" x1="0" y1="0" x2="0" y2="1">
        <stop offset="0" stop-color="#ffffff"/>
        <stop offset="1" stop-color="#e3e6ea"/>
      </linearGradient>
      <radialGradient id="backBlue" cx="0.5" cy="0.3" r="0.8">
        <stop offset="0" stop-color="#3e72e0"/>
        <stop offset="0.6" stop-color="#1f4fc4"/>
        <stop offset="1" stop-color="#12329a"/>
      </radialGradient>
      <radialGradient id="chartGlobe" cx="0.4" cy="0.4" r="0.7">
        <stop offset="0" stop-color="#f2f6fb"/>
        <stop offset="0.6" stop-color="#9fc0e6"/>
        <stop offset="1" stop-color="#2f63c6"/>
      </radialGradient>
      <linearGradient id="portrait" x1="0" y1="0" x2="0" y2="1">
        <stop offset="0" stop-color="#c9a088"/>
        <stop offset="0.5" stop-color="#b48b74"/>
        <stop offset="0.6" stop-color="#2a2e38"/>
        <stop offset="1" stop-color="#1a1c22"/>
      </linearGradient>
    </defs>

    <rect width="447" height="440" fill="url(#backPaper)"/>
    <polygon points="0,152 240,236 447,124 447,440 0,440" fill="url(#backBlue)"/>
    <polyline points="0,140 240,224 447,112" fill="none" stroke="var(--brand-red)" stroke-width="7"/>

    <circle cx="240" cy="184" r="62" fill="#ffffff"/>
    <circle role="img" aria-label="Illustration: rising bar chart with an arrow on a blue globe"
            cx="240" cy="184" r="56" fill="url(#chartGlobe)"/>

    <rect role="img" aria-label="Photo: portrait of Lionel Budwig"
          x="22" y="348" width="68" height="78" fill="url(#portrait)" stroke="#ffffff" stroke-width="2"/>
  </svg>

  <ul class="service-list service-list--left">
    <li><svg width="8" height="8" viewBox="0 0 8 8"><path d="M1 4 L3 6.5 L7 1.5" fill="none" stroke="#1f4fc4" stroke-width="1.6"/></svg>Financial Statements</li>
    <li><svg width="8" height="8" viewBox="0 0 8 8"><path d="M1 4 L3 6.5 L7 1.5" fill="none" stroke="#1f4fc4" stroke-width="1.6"/></svg>Tax Returns</li>
    <li><svg width="8" height="8" viewBox="0 0 8 8"><path d="M1 4 L3 6.5 L7 1.5" fill="none" stroke="#1f4fc4" stroke-width="1.6"/></svg>CFO/Controller services</li>
    <li><svg width="8" height="8" viewBox="0 0 8 8"><path d="M1 4 L3 6.5 L7 1.5" fill="none" stroke="#1f4fc4" stroke-width="1.6"/></svg>Budgeting and Forecasting</li>
    <li><svg width="8" height="8" viewBox="0 0 8 8"><path d="M1 4 L3 6.5 L7 1.5" fill="none" stroke="#1f4fc4" stroke-width="1.6"/></svg>Cash Management</li>
  </ul>
  <ul class="service-list service-list--right">
    <li><svg width="8" height="8" viewBox="0 0 8 8"><path d="M1 4 L3 6.5 L7 1.5" fill="none" stroke="#1f4fc4" stroke-width="1.6"/></svg>Payroll / AP/ AR</li>
    <li><svg width="8" height="8" viewBox="0 0 8 8"><path d="M1 4 L3 6.5 L7 1.5" fill="none" stroke="#1f4fc4" stroke-width="1.6"/></svg>Insurance Analysis</li>
    <li><svg width="8" height="8" viewBox="0 0 8 8"><path d="M1 4 L3 6.5 L7 1.5" fill="none" stroke="#1f4fc4" stroke-width="1.6"/></svg>Cost Analysis</li>
    <li><svg width="8" height="8" viewBox="0 0 8 8"><path d="M1 4 L3 6.5 L7 1.5" fill="none" stroke="#1f4fc4" stroke-width="1.6"/></svg>Special projects</li>
  </ul>

  <h2 class="back-headline">ACCOUNTING/TAX/CONSULTING</h2>
  <p class="back-subline">Services include but not limited to</p>

  <div class="back-contact">
    <p class="back-contact__name">Lionel Budwig, CPA</p>
    <p class="back-contact__line">318 N Willowbrook Ln. Orange Grove, Ca. 92800</p>
    <p class="back-contact__line">555-014-2290</p>
  </div>

  <div class="stamp-box" aria-label="Stamp area"></div>
  <div class="address-line" style="top:197px"></div>
  <div class="address-line" style="top:229px"></div>
  <div class="address-line" style="top:261px"></div>
</section>

</body>
</html>
```